Business Card Design for Law firm - already have logo

Now that we have a logo, we need a business card design - our logo is attached -it is salaryman font if that helps - we would like a file that can be uploaded to cardquill (www.cardquill-example.com) using the logo and with the following information on it:
Quenby Law Firm, P.C.
Delwyn Quenby, Esq.
5817 SW 19th Ave.
Alderhaven, OR 97099
971.555.0142 phone
971.555.0187 fax
del@quenby-example.net
Skype: delquenby
Google talk: delwyn.quenby@mailbox-example.com
Target Market(s)
our business cards are distributed to corporate executives, technology professionals and healthcare providers
Industry/Entity Type
Business
Look and feel

```html
<!DOCTYPE html>
<html lang="en">
<head>
<meta charset="utf-8">
<title>Quenby Law Firm, P.C. – Business Card</title>
<link rel="stylesheet" href="https://fonts.googleapis.com/css2?family=Montserrat:wght@300&family=Open+Sans:wght@400;600&display=swap">
<style>
  :root {
    --backdrop: #9b9c9e;
    --card: #ffffff;
    --ink: #141414;
    --ink-soft: #2a2a2a;
    --shadow: rgba(0, 0, 0, 0.28);
  }
  * { box-sizing: border-box; margin: 0; padding: 0; }
  html, body {
    width: 1200px; height: 900px; overflow: hidden;
    background: var(--backdrop);
  }
  .canvas {
    width: 1200px; height: 900px;
    display: flex; flex-direction: column; align-items: center; justify-content: center;
    gap: 40px;
  }
  .card {
    width: 600px; height: 343px;
    background: var(--card);
    box-shadow: 0 6px 18px var(--shadow);
    position: relative;
    color: var(--ink);
    font-family: "Open Sans", sans-serif;
  }
  /* Front */
  .card--front {
    display: flex; flex-direction: column; align-items: center; justify-content: center;
  }
  .brand-mark { display: flex; align-items: center; gap: 18px; }
  .brand-mark__square { width: 34px; height: 34px; background: var(--ink); }
  .brand-mark__name {
    font-family: "Montserrat", sans-serif; font-weight: 300;
    font-size: 46px; letter-spacing: 12px; color: var(--ink);
  }
  .front-url {
    margin-top: 34px;
    font-family: "Montserrat", sans-serif; font-weight: 300;
    font-size: 13px; letter-spacing: 5px; color: var(--ink-soft);
  }
  /* Back */
  .card--back { padding: 44px 40px 0 46px; }
  .firm-name {
    font-family: "Montserrat", sans-serif; font-weight: 300;
    font-size: 21px; letter-spacing: 3px; color: var(--ink);
  }
  .contact {
    margin-left: 130px; margin-top: 10px;
    font-size: 12.5px; line-height: 1.25; color: var(--ink-soft);
  }
  .contact__name { font-size: 17px; font-weight: 600; color: var(--ink); }
  .contact__suffix { font-size: 10px; margin-left: 72px; }
  .contact__address { margin-top: 12px; }
  .contact__lines { margin-top: 6px; }
  .contact__handles {
    display: flex; gap: 14px; align-items: center; margin-top: 18px; margin-left: -24px;
  }
  .handle { display: flex; align-items: center; gap: 5px; }
  .handle__icon { width: 12px; height: 12px; background: var(--ink); border-radius: 2px; }
  .handle__icon--round { border-radius: 50%; }
  .back-brand {
    position: absolute; right: 150px; bottom: 34px;
    font-family: "Montserrat", sans-serif; font-weight: 300;
    font-size: 16px; letter-spacing: 5px; color: var(--ink);
  }
</style>
</head>
<body>
  <main class="canvas">
    <section class="card card--front" aria-label="Card front">
      <div class="brand-mark">
        <span class="brand-mark__square"></span>
        <span class="brand-mark__name">QUENBY</span>
      </div>
      <p class="front-url">WWW.QUENBY-EXAMPLE.NET</p>
    </section>

    <section class="card card--back" aria-label="Card back">
      <h1 class="firm-name">QUENBY LAW FIRM, P.C.</h1>
      <div class="contact">
        <p class="contact__name">Delwyn Quenby,</p>
        <p class="contact__suffix">Esq.</p>
        <p class="contact__address">5817 SW 19th Ave.<br>Alderhaven, OR 97099</p>
        <p class="contact__lines">PH: 971.555.0142 &nbsp;/&nbsp; FAX: 971.555.0187<br>del@quenby-example.net</p>
        <div class="contact__handles">
          <span class="handle"><span class="handle__icon"></span>delquenby</span>
          <span class="handle"><span class="handle__icon handle__icon--round"></span>delwyn.quenby@mailbox-example.com</span>
        </div>
      </div>
      <p class="back-brand">QUENBY</p>
    </section>
  </main>
</body>
</html>
```